Business Card Design needed for logo design project

Our business needs a business card design. I'm not sure what format files are generally delivered back, but clearly I will need the ability to edit to add colleagues contact details.

Our logo is attached.

Brivomar is a 3D design services company, providing app, serious/educational game, VR and AR websites/applications to corporate clients.

Target Market(s)

Corporate blue-chip clients needing 3D design services

Industry/Entity Type

Business

Font styles to use
Sans Serif

Requirements
Must have
• Templated such that I can add details (name, phone number etc). Needs to include logo from previous project winner - attached.

```html
<!DOCTYPE html>
<html lang="en">
<head>
<meta charset="utf-8">
<title>Brivomar Business Card</title>
<link rel="stylesheet" href="https://fonts.googleapis.com/css2?family=Open+Sans:wght@400;600&display=swap">
<style>
  :root {
    --backdrop: #c4c4c4;
    --card-white: #ffffff;
    --brand-red: #e81e2a;
    --wave-red: #f27a6a;
    --ink: #333333;
    --ink-logo: #2b2b2b;
    --paper-white: #ffffff;
  }
  html, body {
    margin: 0;
    width: 1200px;
    height: 900px;
    overflow: hidden;
    background: var(--backdrop);
    font-family: "Open Sans", sans-serif;
  }
  .sheet {
    position: relative;
    width: 1200px;
    height: 900px;
  }
  .card {
    position: absolute;
    left: 250px;
    width: 700px;
    height: 400px;
    overflow: hidden;
    box-shadow: 0 8px 24px rgba(0,0,0,0.18);
  }
  .card--back { top: 28px; background: var(--brand-red); }
  .card--front { top: 466px; background: var(--card-white); }

  .card__pattern {
    position: absolute;
    left: 0;
    width: 700px;
  }
  .card--back .card__pattern {
    top: 60px;
    height: 260px;
    background: linear-gradient(180deg,
      rgba(255,255,255,0) 0%,
      rgba(255,255,255,0.14) 50%,
      rgba(255,255,255,0) 100%);
  }
  .card--front .card__pattern {
    top: 150px;
    height: 140px;
    background: linear-gradient(180deg,
      rgba(242,122,106,0) 0%,
      rgba(242,122,106,0.22) 50%,
      rgba(242,122,106,0) 100%);
  }

  .brand {
    position: absolute;
    display: flex;
    align-items: center;
    gap: 14px;
  }
  .brand__dot {
    width: 50px;
    height: 50px;
    border-radius: 50%;
  }
  .brand__name {
    font-weight: 400;
    font-size: 46px;
    letter-spacing: 4px;
    text-transform: uppercase;
    line-height: 1;
  }
  .card--back .brand { left: 130px; top: 150px; }
  .card--back .brand__dot { background: var(--paper-white); }
  .card--back .brand__name { color: var(--paper-white); }

  .card--front .brand { left: 50%; transform: translateX(-50%); top: 62px; }
  .card--front .brand__dot { background: var(--brand-red); }
  .card--front .brand__name { color: var(--ink-logo); }

  .contact {
    position: absolute;
    margin: 0;
    font-size: 17px;
    line-height: 1.35;
    color: var(--ink);
  }
  .contact--left { left: 40px; bottom: 62px; }
  .contact--right { right: 40px; bottom: 30px; text-align: right; }
</style>
</head>
<body>
<main class="sheet">

  <section class="card card--back" aria-label="Card back">
    <div class="card__pattern" role="img" aria-label="Decorative flowing band of fine white wave lines"></div>
    <div class="brand">
      <span class="brand__dot"></span>
      <span class="brand__name">Brivomar</span>
    </div>
  </section>

  <section class="card card--front" aria-label="Card front">
    <div class="brand">
      <span class="brand__dot"></span>
      <span class="brand__name">Brivomar</span>
    </div>
    <div class="card__pattern" role="img" aria-label="Decorative flowing band of fine red wave lines"></div>
    <p class="contact contact--left">E-mail: hello@brivomar.com<br>Tel: 555 214</p>
    <p class="contact contact--right">Web: brivomar.com<br>Fax: 555 214 7</p>
  </section>

</main>
</body>
</html>
```